Business cards / Stationery
Stationery
Professional
Tomas Belcourt
DOE, CPT, LMT
1400 North Pelham Road
Austin, Texas 78756
tomas.belcourt@merrowcareclinic.com
www.merrowcareclinic.com

```html
<!DOCTYPE html>
<html lang="en">
<head>
<meta charset="utf-8">
<title>Merrow Care – Stationery</title>
<link href="https://fonts.googleapis.com/css2?family=Roboto:wght@400;700;900&family=Open+Sans:wght@400;600&display=swap" rel="stylesheet">
<style>
:root{
  --blue:#1aa0dc;
  --blue-deep:#0b7fc0;
  --blue-light:#7fd0f2;
  --grey:#8e9196;
  --grey-dark:#6c6f74;
  --ink:#3d3f42;
  --paper:#ffffff;
  --bg:#ebebeb;
  --brand-blue:#1c8fd0;
}
*{margin:0;padding:0;box-sizing:border-box}
html,body{width:1200px;height:821px;overflow:hidden;background:var(--bg)}
body{position:relative;font-family:"Open Sans",Arial,sans-serif;color:var(--ink)}
.sheet{position:absolute;background:var(--paper);box-shadow:0 1px 3px rgba(0,0,0,.18);overflow:hidden}
.sheet svg.art{position:absolute;inset:0;width:100%;height:100%}
.brand{position:absolute;display:flex;flex-direction:column;align-items:center;text-align:center}
.brand-dot{border-radius:50%;background:var(--grey-dark)}
.brand-name{font-family:"Roboto",Arial,sans-serif;font-weight:900;color:var(--brand-blue);letter-spacing:.02em;line-height:1;white-space:nowrap}
.brand-tag{font-family:"Roboto",Arial,sans-serif;font-weight:700;color:var(--grey);letter-spacing:.06em;white-space:nowrap;text-transform:uppercase}
.brand.on-dark .brand-name,.brand.on-dark .brand-tag{color:#fff}
.brand.on-dark .brand-dot{background:#fff}

/* letterhead */
.letterhead{left:67px;top:43px;width:497px;height:739px}
.letterhead .brand{left:52px;top:22px}
.letterhead .brand-dot{width:34px;height:34px;margin-bottom:5px}
.letterhead .brand-name{font-size:15px}
.letterhead .brand-tag{font-size:4px;margin-top:2px}
.letterhead-contact{position:absolute;left:221px;top:8px;font-size:6.4px;line-height:10px;color:var(--ink);font-style:normal}
.letterhead-watermark{position:absolute;left:85px;top:217px;width:272px;height:272px;border-radius:50%;background:#f1f5f8}

/* cards */
.card{width:216px;height:132px;border-radius:7px}
.card-front{left:612px;top:91px}
.card-back{left:845px;top:91px}
.card-grey{left:612px;top:233px;background:linear-gradient(180deg,#9a9da1,#76797e)}
.card-blue{left:845px;top:233px;background:linear-gradient(180deg,#29aee6,#0b86c8)}
.card .brand-dot{width:24px;height:24px;margin-bottom:4px}
.card .brand-name{font-size:11px}
.card .brand-tag{font-size:3.4px;margin-top:2px}
.card-front .brand{left:8px;top:52px}
.card-front .brand-dot{width:20px;height:20px;margin-bottom:3px}
.card-front .brand-name{font-size:9px}
.card-front .brand-tag{font-size:2.8px}
.card-person{position:absolute;left:124px;top:8px;text-align:center;width:86px}
.card-person .name{font-family:"Roboto",Arial,sans-serif;font-weight:700;font-size:9px;color:var(--brand-blue)}
.card-person .title{font-size:5px;color:var(--grey-dark)}
.card-contact{position:absolute;left:126px;top:62px;font-size:4.2px;line-height:8px}
.card-contact li{list-style:none;display:flex;align-items:center;gap:3px;white-space:nowrap}
.card-contact .ico{width:4px;height:4px;border-radius:50%;background:var(--blue);flex:none}
.card-centered .brand{left:0;right:0;top:26px}
.card-web{position:absolute;left:0;right:0;bottom:16px;text-align:center;font-size:5px}
.card-back .card-web{bottom:38px;color:var(--grey-dark)}
.card-grey .card-web{color:#fff}

/* envelope */
.envelope{left:595px;top:403px;width:581px;height:379px}
</style>
</head>
<body>

<section class="sheet letterhead">
  <svg class="art" viewBox="0 0 497 739" preserveAspectRatio="none" aria-hidden="true">
    <path d="M0 0 H40 C30 180 20 300 48 430 C70 540 58 640 34 739 H0 Z" fill="var(--blue)"/>
    <path d="M48 430 C70 540 58 640 34 739 H22 C46 640 58 540 40 450 Z" fill="var(--blue-light)" opacity=".7"/>
    <path d="M56 470 C80 560 72 650 50 739 H42 C64 650 70 560 52 480 Z" fill="var(--grey)"/>
  </svg>
  <div class="letterhead-watermark"></div>
  <div class="brand">
    <div class="brand-dot"></div>
    <div class="brand-name">MERROW CARE</div>
    <div class="brand-tag">Integrative Care Therapy</div>
  </div>
  <address class="letterhead-contact">
    1400 North Pelham Road<br>
    Austin, Texas 78756<br>
    T (512) 555-0142<br>
    F (512) 555-0143<br>
    tomas.belcourt@merrowcareclinic.com<br>
    www.merrowcareclinic.com
  </address>
</section>

<section class="sheet card card-front">
  <svg class="art" viewBox="0 0 216 132" preserveAspectRatio="none" aria-hidden="true">
    <path d="M80 0 H100 C92 40 126 66 116 132 H98 C108 66 74 40 80 0 Z" fill="var(--blue)"/>
    <path d="M100 0 H105 C97 40 131 66 121 132 H116 C126 66 92 40 100 0 Z" fill="var(--grey)" opacity=".6"/>
  </svg>
  <div class="brand">
    <div class="brand-dot"></div>
    <div class="brand-name">MERROW CARE</div>
    <div class="brand-tag">Integrative Care Therapy</div>
  </div>
  <div class="card-person">
    <div class="name">Tomas Belcourt</div>
    <div class="title">DOE, CPT, LMT</div>
  </div>
  <ul class="card-contact">
    <li><span class="ico"></span>1400 North Pelham Road</li>
    <li><span class="ico"></span>Austin, Texas 78756</li>
    <li><span class="ico"></span>T (512) 555-0142</li>
    <li><span class="ico"></span>tomas.belcourt@merrowcareclinic.com</li>
  </ul>
</section>

<section class="sheet card card-back card-centered">
  <div class="brand">
    <div class="brand-dot"></div>
    <div class="brand-name">MERROW CARE</div>
    <div class="brand-tag">Integrative Care Therapy</div>
  </div>
  <div class="card-web">www.merrowcareclinic.com</div>
</section>

<section class="sheet card card-grey card-centered">
  <div class="brand on-dark">
    <div class="brand-dot"></div>
    <div class="brand-name">MERROW CARE</div>
    <div class="brand-tag">Integrative Care Therapy</div>
  </div>
  <div class="card-web">www.merrowcareclinic.com</div>
</section>

<section class="sheet card card-blue card-centered">
  <div class="brand on-dark">
    <div class="brand-dot"></div>
    <div class="brand-name">MERROW CARE</div>
    <div class="brand-tag">Integrative Care Therapy</div>
  </div>
</section>

<section class="sheet envelope">
  <svg class="art" viewBox="0 0 581 379" preserveAspectRatio="none" aria-hidden="true">
    <defs>
      <linearGradient id="flap" x1="0" y1="0" x2="0" y2="1">
        <stop offset="0" stop-color="var(--blue)"/>
        <stop offset="1" stop-color="var(--blue-deep)"/>
      </linearGradient>
    </defs>
    <path d="M0 0 H581 V30 H150 C90 30 60 60 40 120 C30 150 14 165 0 170 Z" fill="url(#flap)"/>
    <path d="M0 176 C20 170 36 152 46 124 C66 66 96 36 150 36 H581 V42 H152 C100 42 72 70 54 126 C44 158 24 178 0 184 Z" fill="var(--grey)" opacity=".55"/>
  </svg>
</section>

</body>
</html>
```